We need a business card design for an assisted living facility in Los Angeles. We have a logo selected but we would like a business card design that will leave a lasting impression on families looking to place their elderly loved ones in our care as well as on other facility providers who may refer their elderly residents to our facility.

```html
<!DOCTYPE html>
<html lang="en">
<head>
<meta charset="utf-8">
<title>Harborview Crest Senior Living – Business Card</title>
<link href="https://fonts.googleapis.com/css2?family=Cinzel:wght@400&family=Karla:wght@400&display=swap" rel="stylesheet">
<style>
  :root{
    --bg:#c9cacc;
    --card-white:#ffffff;
    --brand-blue:#1f72b6;
    --brand-blue-light:#3d8ac7;
    --ink-grey:#6d6f72;
    --rule-grey:#9a9c9f;
    --on-blue:#ffffff;
  }
  *{box-sizing:border-box;margin:0;padding:0}
  html,body{width:1200px;height:876px;overflow:hidden}
  body{background:var(--bg);position:relative;font-family:"Karla",Arial,sans-serif}
  .card{position:absolute;top:290px;width:520px;height:297px;box-shadow:0 6px 18px rgba(0,0,0,.18)}
  .card--front{left:50px;background:var(--card-white)}
  .card--back{left:630px;background:var(--brand-blue);overflow:hidden}

  .wordmark{position:absolute;text-align:center;font-family:"Cinzel",Georgia,serif;font-weight:400;color:var(--brand-blue)}
  .wordmark__name{display:block;font-size:31px;letter-spacing:1px;line-height:1}
  .wordmark__tag{display:block;font-size:11px;letter-spacing:7px;margin-top:8px}
  .card--front .wordmark{left:170px;top:38px;width:320px}
  .card--front .wordmark__name{font-size:27px}

  .person{position:absolute;left:190px;top:135px;width:250px;text-align:center}
  .person__name{font-family:"Cinzel",Georgia,serif;font-size:22px;color:var(--brand-blue);letter-spacing:1px}
  .person__role{display:flex;align-items:center;gap:8px;margin-top:6px;font-size:12px;color:var(--ink-grey)}
  .person__role::before,.person__role::after{content:"";flex:1;height:1px;background:var(--rule-grey)}

  .contact{position:absolute;left:28px;top:40px;list-style:none;font-size:12px;color:var(--ink-grey)}
  .contact li{display:flex;align-items:center;gap:6px;margin-bottom:6px}
  .contact svg{width:10px;height:10px;fill:var(--brand-blue)}

  .address{position:absolute;right:40px;bottom:38px;font-size:14px;line-height:1.5;color:var(--ink-grey);text-align:left}

  .card--back .map-field{position:absolute;left:120px;top:20px;width:320px;height:250px;border-radius:50%;
    background:radial-gradient(ellipse at center,rgba(255,255,255,.22),rgba(255,255,255,0) 70%)}
  .card--back .wordmark{left:60px;top:110px;width:400px;color:var(--on-blue)}
</style>
</head>
<body>
  <section class="card card--front" aria-label="Business card front">
    <ul class="contact">
      <li><svg viewBox="0 0 10 10"><path d="M2 0l2 2-1 1.5c.6 1.3 1.8 2.5 3.5 3.5L8 6l2 2-1.5 2C4 9.5.5 6 0 1.5z"/></svg>555-014-2290</li>
      <li><svg viewBox="0 0 10 10"><path d="M0 2h10v6H0zM0 2l5 3.5L10 2" /></svg>info@harborviewcrest.com</li>
      <li><svg viewBox="0 0 10 10"><circle cx="5" cy="5" r="5"/></svg>www.harborviewcrest.com</li>
    </ul>
    <div class="wordmark">
      <span class="wordmark__name">HARBORVIEW CREST</span>
      <span class="wordmark__tag">SENIOR LIVING</span>
    </div>
    <div class="person">
      <p class="person__name">DANIEL R HALE</p>
      <p class="person__role">President</p>
    </div>
    <address class="address" style="font-style:normal">1180 Maple Grove Avenue<br>Pasadena, CA 91101</address>
  </section>

  <section class="card card--back" aria-label="Business card back">
    <div class="map-field" role="img" aria-label="Faint dotted world map behind the name"></div>
    <div class="wordmark">
      <span class="wordmark__name">HARBORVIEW CREST</span>
      <span class="wordmark__tag">SENIOR LIVING</span>
    </div>
  </section>
</body>
</html>
```